Mobile App Screen Design for Dog Kennels App

Design a single home page design for an iphone app.

A PhotoShop file must be provided with all layers individually available so they can be modified.

The customers website
http://www.brindlewoodhoundhouse-example.com/
and Facebook account
https://www.facebook.com/Brindlewood-Hound-House-913274058216437/?fref=ts
can be used for reference.

The company name "Brindlewood Hound House" should appear on the home page other than that there is free reign on the design.

Any questions let me know.

```html
<!DOCTYPE html>
<html lang="en">
<head>
<meta charset="utf-8">
<title>Brindlewood Hound House – Home</title>
<link rel="stylesheet" href="https://fonts.googleapis.com/css2?family=Arimo:wght@400;700&family=Comic+Neue:ital,wght@0,700;1,700&display=swap">
<style>
  :root {
    --cream: #fdeadb;
    --ink: #111111;
    --status-grey: #7a7a7a;
    --forest: #4a6b4f;
    --brick: #e0341e;
    --white: #ffffff;
    --art-warm: #8a6a4f;
    --art-soft: #d9b898;
  }
  html, body {
    margin: 0;
    padding: 0;
    width: 1200px;
    height: 2239px;
    overflow: hidden;
    background: var(--cream);
  }
  .home-screen {
    position: relative;
    width: 1200px;
    height: 2239px;
    background: var(--cream);
    overflow: hidden;
    font-family: "Arimo", Arial, sans-serif;
  }
  .status-bar {
    position: absolute;
    top: 44px;
    left: 24px;
    right: 24px;
    height: 44px;
    display: flex;
    align-items: center;
    justify-content: space-between;
    color: var(--status-grey);
    font-size: 34px;
  }
  .status-bar .carrier,
  .status-bar .battery {
    display: flex;
    align-items: center;
    gap: 12px;
  }
  .status-bar .time {
    position: absolute;
    left: 50%;
    transform: translateX(-50%);
  }
  .welcome {
    position: absolute;
    top: 490px;
    width: 100%;
    text-align: center;
    font-weight: 700;
    font-size: 42px;
    line-height: 1.2;
    letter-spacing: 1px;
    color: var(--ink);
    margin: 0;
  }
  .business-name {
    position: absolute;
    top: 543px;
    width: 100%;
    text-align: center;
    font-weight: 700;
    font-size: 84px;
    line-height: 1.2;
    color: var(--ink);
    margin: 0;
    letter-spacing: -0.5px;
    white-space: nowrap;
  }
  .tagline {
    position: absolute;
    top: 645px;
    width: 100%;
    text-align: center;
    font-family: "Comic Neue", "Comic Sans MS", cursive;
    font-weight: 700;
    font-style: italic;
    font-size: 72px;
    line-height: 1.2;
    color: var(--forest);
    margin: 0;
    white-space: nowrap;
  }
  .hero-art {
    position: absolute;
    top: 852px;
    left: 130px;
    width: 940px;
    height: 674px;
    border-radius: 40px;
    background: radial-gradient(ellipse at 45% 55%, var(--art-soft) 0%, var(--art-warm) 100%);
  }
  .boarding-button {
    position: absolute;
    top: 1603px;
    left: 262px;
    width: 674px;
    height: 160px;
    border-radius: 20px;
    background: var(--brick);
    color: var(--white);
    font-family: "Comic Neue", "Comic Sans MS", cursive;
    font-weight: 700;
    font-size: 68px;
    display: flex;
    align-items: center;
    justify-content: center;
    text-decoration: none;
    letter-spacing: 1px;
    white-space: nowrap;
  }
  .corner-wave {
    position: absolute;
    left: 0;
    top: 0;
  }
  .learn-more {
    position: absolute;
    left: 920px;
    top: 2075px;
    width: 260px;
    display: flex;
    flex-direction: column;
    align-items: center;
    color: var(--white);
    text-decoration: none;
    font-family: "Comic Neue", "Comic Sans MS", cursive;
    font-weight: 700;
    font-size: 48px;
    line-height: 1;
    white-space: nowrap;
  }
  .learn-more svg { margin-bottom: 14px; }
</style>
</head>
<body>
<main class="home-screen">
  <div class="status-bar">
    <span class="carrier">
      <svg width="118" height="22" viewBox="0 0 118 22" aria-hidden="true">
        <circle cx="11" cy="11" r="10" fill="#7a7a7a"/>
        <circle cx="35" cy="11" r="10" fill="#7a7a7a"/>
        <circle cx="59" cy="11" r="10" fill="#7a7a7a"/>
        <circle cx="83" cy="11" r="10" fill="#7a7a7a"/>
        <circle cx="107" cy="11" r="9" fill="none" stroke="#7a7a7a" stroke-width="2"/>
      </svg>
      Carrier
    </span>
    <span class="time">5:30PM</span>
    <span class="battery">
      100%
      <svg width="74" height="32" viewBox="0 0 74 32" aria-hidden="true">
        <rect x="1.5" y="1.5" width="64" height="29" rx="4" fill="none" stroke="#7a7a7a" stroke-width="3"/>
        <rect x="6" y="6" width="55" height="20" rx="2" fill="#7a7a7a"/>
        <rect x="67" y="10" width="5" height="12" rx="1" fill="#7a7a7a"/>
      </svg>
    </span>
  </div>

  <p class="welcome">WELCOME TO</p>
  <h1 class="business-name">Brindlewood Hound House</h1>
  <p class="tagline">~ Dog Kennels you can trust ~</p>

  <div class="hero-art" role="img" aria-label="Cartoon illustration of a happy brown dog sitting beside a wooden kennel with a green roof and a red food bowl"></div>

  <a class="boarding-button" href="#boarding">BOARDING →</a>

  <svg class="corner-wave" width="1200" height="2239" viewBox="0 0 1200 2239" aria-hidden="true">
    <defs>
      <filter id="wave-shadow" x="-10%" y="-10%" width="120%" height="120%">
        <feDropShadow dx="-4" dy="-4" stdDeviation="8" flood-color="#000" flood-opacity="0.35"/>
      </filter>
    </defs>
    <path d="M 545 2239 C 900 2239 1180 1950 1200 1570 L 1200 2239 Z" fill="#4a6b4f" filter="url(#wave-shadow)"/>
  </svg>

  <a class="learn-more" href="#menu">
    <svg width="80" height="60" viewBox="0 0 80 60" aria-hidden="true">
      <rect x="0" y="0" width="80" height="12" rx="6" fill="#ffffff"/>
      <rect x="0" y="24" width="80" height="12" rx="6" fill="#ffffff"/>
      <rect x="0" y="48" width="80" height="12" rx="6" fill="#ffffff"/>
    </svg>
    <span class="learn-more-label">learn more</span>
  </a>
</main>
</body>
</html>
```